Bright Meadow Cabins Needs A Flyer

We need a flyer for our newest product "The Sunlit Garden Workpod Deluxe"

Here is some copy for the flyer:

1. More and more people everyday are working from home and finding it difficult to disconnect from home activities in order to focus on their work. They are also finding it very expensive to add on to their existing house for a quiet place. Our archatectually stunning, Sunlit Garden Workpod Deluxe is the answer. The office studio measures 16' wide and 10' deep. 160 Square feet of space.

Perfect for dozens of purposes. Home office, design studio, artist studio, home school office, reading room, craft studio, drafting room.

Features include:

- Steel Framing. 40-60% lighter then wood, higher strength to weight ratio, resistant to mold and fire and steel is the most recycled material on earth!
- Spray foam insulation. Cool in the summer and warm in the winter.
- HVAC Mini Split with wireless remote control and thermostat.
- 100% Off grid with enough solar and battery storage to run your entire office. No need to pay for an expensive electric installation.
- Flush fitting floor outlets to reduce wires.
- TV mount (Optional with pre-wired electric, HDMI, digital audio & Cat 6)
- Windows are tempered glass custom made by Vorn Glazing.
- Solar qualifies for a 26% tax credit. This is not a write-off rather it is a direct reduction on your tax obligation.
- Thousands of dollars less than adding onto your home.
- Custom color, siding, features available.

This beautiful back yard office is delivered 100% assembled and ready to enjoy on the day of delivery.

We ship nationwide from our factory in South Carolina. Give us a call anytime to speak to a designer and start your dream office today!

555-318-4720
info@BrightMeadowCabins.example

```html
<!DOCTYPE html>
<html lang="en">
<head>
<meta charset="utf-8">
<title>Bright Meadow Cabins – Sunlit Garden Workpod Deluxe Flyer</title>
<link href="https://fonts.googleapis.com/css2?family=Figtree:wght@400;500;700;800&family=Lato:wght@400;700&display=swap" rel="stylesheet">
<style>
  :root {
    --backdrop: #575757;
    --paper: #ffffff;
    --sun: #f3b12f;
    --leaf: #4f9a3c;
    --leaf-dark: #3f7f30;
    --leaf-light: #62a84a;
    --ink: #111111;
    --ink-soft: #222222;
  }
  * { margin: 0; padding: 0; box-sizing: border-box; }
  html, body { width: 1200px; height: 1200px; overflow: hidden; }
  body { background: var(--backdrop); position: relative; }

  .flyer {
    position: absolute; left: 133px; top: 0;
    width: 934px; height: 1200px;
    background: var(--paper);
    overflow: hidden;
    font-family: "Figtree", sans-serif;
    color: var(--ink);
  }
  .flyer-shapes { position: absolute; inset: 0; width: 100%; height: 100%; }

  .brand {
    position: absolute; left: 600px; top: 226px; width: 330px;
    display: flex; align-items: center; gap: 10px;
  }
  .brand-dot { width: 22px; height: 22px; border-radius: 50%; background: var(--sun); flex: none; }
  .brand-name {
    font-family: "Figtree", sans-serif; font-weight: 800;
    font-size: 27px; color: var(--leaf-dark); letter-spacing: 0.3px;
  }

  .frame-drawing {
    position: absolute; left: 455px; top: 322px; width: 455px; height: 244px;
    background: linear-gradient(180deg, #f2f2f2 0%, #d9d9d9 80%, #b9a58f 100%);
  }

  .headline {
    position: absolute; left: 27px; top: 555px; width: 460px;
    font-weight: 800; font-size: 40px; line-height: 44px; text-transform: uppercase;
    color: var(--ink);
  }
  .intro {
    position: absolute; left: 27px; top: 648px; width: 440px;
    font-family: "Lato", sans-serif; font-size: 15.8px; line-height: 19.4px; color: var(--ink-soft);
  }
  .intro strong { font-weight: 700; }
  .uses {
    position: absolute; left: 27px; top: 793px; width: 430px;
    font-weight: 700; font-size: 14.6px; line-height: 19.5px;
  }
  .exterior-photo {
    position: absolute; left: 63px; top: 867px; width: 359px; height: 201px;
    border: 3px solid var(--paper);
    background: linear-gradient(180deg, #b9d3e6 0%, #7f9e6a 45%, #4a5a40 70%, #6f8f47 100%);
  }
  .shipping {
    position: absolute; left: 27px; top: 1080px; width: 460px;
    font-size: 14px; line-height: 18px; color: var(--ink-soft);
  }
  .contact {
    position: absolute; left: 35px; top: 1124px;
    display: flex; align-items: center; gap: 16px;
    font-weight: 700; font-size: 15.5px;
  }
  .contact-item { display: flex; align-items: center; gap: 6px; }
  .contact-item svg { width: 18px; height: 18px; }

  .features-tab {
    position: absolute; left: 492px; top: 594px; width: 295px; height: 50px;
    background: var(--leaf); border-radius: 0 25px 25px 0;
    color: #fff; font-weight: 800; font-size: 23px; line-height: 50px;
    padding-left: 12px; text-transform: uppercase;
  }
  .features-tab::after {
    content: ""; position: absolute; left: 30px; right: 10px; bottom: -8px; height: 4px;
    background: linear-gradient(90deg, rgba(0,0,0,0.25), rgba(0,0,0,0));
    border-radius: 2px;
  }
  .feature-list {
    position: absolute; left: 536px; top: 676px; width: 372px;
    list-style: none; font-size: 13.6px; line-height: 17.8px; color: var(--ink-soft);
  }
  .feature-list li { position: relative; margin-bottom: 9px; }
  .feature-list li::before {
    content: ""; position: absolute; left: -34px; top: 3px;
    width: 12px; height: 12px; border-radius: 50%; background: var(--leaf-light);
  }
  .delivery-note {
    position: absolute; left: 513px; top: 1120px; width: 390px;
    font-size: 15.5px; line-height: 20px; color: var(--ink-soft);
  }
  .delivery-note strong { font-weight: 700; }
</style>
</head>
<body>
<main class="flyer">
  <svg class="flyer-shapes" viewBox="0 0 1262 1622" preserveAspectRatio="none" aria-hidden="true">
    <defs>
      <linearGradient id="heroTones" x1="0" y1="0" x2="0" y2="1">
        <stop offset="0" stop-color="#a9cbe8"/>
        <stop offset="0.25" stop-color="#5c6b5a"/>
        <stop offset="0.55" stop-color="#c9c3b4"/>
        <stop offset="0.85" stop-color="#6d8a4c"/>
        <stop offset="1" stop-color="#8a9a7a"/>
      </linearGradient>
    </defs>
    <polygon class="hero-band" points="1040,0 1075,0 665,745 0,668 0,660 620,640" fill="#5aa443"/>
    <polygon class="hero-shade" points="0,668 620,640 665,745" fill="#437f32"/>
    <polygon class="orange-panel" points="0,668 665,745 665,1622 0,1622" fill="#f3b12f"/>
    <polygon class="footer-wedge" points="0,1545 0,1622 500,1622" fill="#4f9a3c"/>
  </svg>
  <svg class="flyer-shapes" viewBox="0 0 1262 1622" preserveAspectRatio="none" role="img" aria-label="Photo of the garden workpod with glass front, wooden doors and a furnished office inside, under trees">
    <polygon points="0,0 1040,0 620,640 0,660" fill="url(#heroTones)"/>
  </svg>

  <div class="brand">
    <span class="brand-dot"></span>
    <span class="brand-name">Bright Meadow Cabins</span>
  </div>

  <div class="frame-drawing" role="img" aria-label="Drawing of the steel wall and roof framing of the workpod"></div>

  <h1 class="headline">The Sunlit Garden Workpod Deluxe</h1>
  <p class="intro">More and more people everyday are working from home and finding it difficult to disconnect from home activities in order to focus on their work. They are also finding it very expensive to add on to their existing house for a quiet place. Our archatectually stunning, Sunlit Garden Workpod Deluxe is the answer. The office studio measures <strong>16' wide and 10' deep. 160 Square feet of space.</strong></p>
  <p class="uses">Perfect for dozens of purposes. Home office, design studio, artist studio, home school office, reading room, craft studio, drafting room.</p>

  <div class="exterior-photo" role="img" aria-label="Photo of the workpod from the side with solar panels on the roof, in a planted garden"></div>

  <p class="shipping">We ship nationwide from our factory in South Carolina. Give us a call anytime to speak to a designer and start your dream office today !</p>
  <div class="contact">
    <span class="contact-item">
      <svg viewBox="0 0 20 20" aria-hidden="true"><circle cx="10" cy="10" r="8.5" fill="none" stroke="#111" stroke-width="1.4"/><path d="M7 5.5l1.6 2-1 1.2c.6 1.3 1.6 2.3 2.9 2.9l1.2-1 2 1.6-1 1.6c-3.4-.2-6.5-3.3-6.7-6.7z" fill="#111"/></svg>
      555-318-4720
    </span>
    <span class="contact-item">
      <svg viewBox="0 0 20 20" aria-hidden="true"><rect x="1.5" y="4" width="17" height="12" fill="#111"/><path d="M1.5 4l8.5 7 8.5-7" fill="none" stroke="#f3b12f" stroke-width="1.4"/></svg>
      info@BrightMeadowCabins.example
    </span>
  </div>

  <h2 class="features-tab">Features Include :</h2>
  <ul class="feature-list">
    <li>Steel Framing. 40-60% lighter then wood, higher strength to weight ratio, resistant to mold and fire and steel is the most recycled material on earth!</li>
    <li>Spray foam insulation. Cool in the summer and warm in the winter.</li>
    <li>HVAC Mini Split with wireless remote control and thermostat.</li>
    <li>100% Off grid with enough solar and battery storage to run your entire office. No need to pay for an expensive electric installation.</li>
    <li>Flush fitting floor outlets to reduce wires.</li>
    <li>TV mount (Optional with pre-wired electric, HDMI, digital audio &amp; Cat 6)</li>
    <li>Windows are tempered glass custom made by Vorn Glazing.</li>
    <li>Solar qualifies for a 26% tax credit. This is not a write-off rather it is a direct reduction on your tax obligation.</li>
    <li>Thousands of dollars less than adding onto your home.</li>
    <li>Custom color, siding, features available.</li>
  </ul>
  <p class="delivery-note">This beautiful back yard office is delivered <strong>100%</strong> assembled and ready to enjoy on the day of delivery.</p>
</main>
</body>
</html>
```